WORDPRESS WEB DESIGN PROJECT-DESIGN & DEVELOP

OUR BUSINESS
Bright Harbour Consulting provides effective project controls and management solutions for construction projects in Australia and Overseas. We provide services to both large multinational companies and smaller privately owned businesses. Our knowledge and expertise assist clients to effectively plan and manage their construction projects or project portfolios. Our focus is to provide your business with the tools, solutions and strategies necessary to deliver projects on time and within budget.

WHY WE ARE RE-BRANDING OUR WEBSITE
Our existing website design is not effective at promoting our business. We require a fresh, new, innovative approach to effectively market our business brand. Our new website will have the same look and feed as our newly developed business brochure.

DESIGN
Our new website will have the same look and feed as our business brochure. This website will be developed in Word press; a customized theme is required. The graphic design and images will enhance the written content; any graphics need to be developed in Photoshop as this is the software we use. A horizontal navigation menu will be implemented but must blend into the design and not be contained in a colour band. The webpage itself needs to span the entire viewable screen and must not look like an A4 piece of paper on a colored background. Additional design comments have been attached to this project as " website contents" word doc.

WEDSITES I LIKE THE LOOK OF
www.example-tarvion.com (very professional, similar color scheme)
www.example-quellory.com ( Good design, background made the website pop)
www.example-brimwoodfloorcare.com.au (clean,tidy,sharp images)
www.example-velantis.com ( the look was simple but effective)
http://www.example-norvik.com

STYLE
We require a stylish, clean and easy to navigate website, with fresh, exciting and engaging imagery. Our website design needs to be modern, clean and sleek.

WRITTEN CONTENT
New written content for each page is provided with this project, there is 50% less content in this project than the original website.

QUALITY
High resolution images and photos will be used to promote an overall quality, professional look and feel.

FUNCTIONALITY
The design needs to be easily updated and editable. The person updating the webpage content and images does not know coding, so the theme will need to be able to interact with plugins. All design components need to be optimized for indexing on major search engines e.g. Firefox, internet explorer, Google and safari.

ICONS
I will require icon links to Email, Circlebook and LinkedIn, but not for twitter, Gmail or live feeds.

MENU
1.Home
2.Services
3.Benefits
4.Management
5.Planning
6.Optimization
7.Industry
8.Software
9.Contact us
10.Recruitment

TARGET AUDIENCE
Corporate Clients in all industry’s sectors
Supporting clients in
★OIL & Gas
★Iron Ore
★Coal
★New Industries
★Building and Construction
★Rail
★Civil
★Manufacturing
★Petrochemical
★Telecommunications

THE WINNER WILL PROVIDE
1. Wordpress theme with design.
2. List of plugins needed to meet requirements or design.
3. All images used in design.
4. Any custom php, javascript, or css files needed for the design.
5. List of core wordpress files customized as part of the design.
6. Any source files for custom images or design work (psd)

ATTACHMENTS
The following items will be attached to this project
1. Business logo
2. Icon images
3. Business Brochure PDF
4. Business brochure cover page psd file
5. Content required in each webpage

DESIGN AND DEVELOP
This project is to design and develop a word press website. In respect that the chosen designer may not be able to provide the development, 2 places of $400 each have been offered (1st for the design aspect, and 2nd for the development). The winning designer will receive $800 if both design and development have been achieved.

PROJECT CHANGES

The projects budget has increased from $600 to $800

Completion date has extended by 7 day.

Requirements
Should not have
• This design must have not appear out-dated or cluttered
Please do not provide any designs that look like our old website.

```html
<!DOCTYPE html>
<html lang="en">
<head>
<meta charset="utf-8">
<title>Bright Harbour Consulting</title>
<link href="https://fonts.googleapis.com/css2?family=PT+Sans:wght@400;700&display=swap" rel="stylesheet">
<style>
:root{
  --red:#d71920;
  --dark:#2a2a2a;
  --footer:#3d3d3d;
  --text:#3a3a3a;
  --light:#f1f1f3;
  --rule:#d9d9dc;
  --white:#ffffff;
}
*{margin:0;padding:0;box-sizing:border-box}
html,body{width:900px;height:1200px;overflow:hidden}
body{font-family:"PT Sans",sans-serif;color:var(--text);background:var(--light);position:relative}
.abs{position:absolute}
.site-header{left:0;top:0;width:900px;height:100px;background:linear-gradient(#ffffff,#ececee)}
.brand{left:97px;top:34px;display:flex;align-items:center;gap:8px}
.brand-mark{width:22px;height:22px;background:var(--red)}
.brand-name{font-size:24px;font-weight:700;color:var(--dark);letter-spacing:-.3px}
.brand-tag{left:127px;top:62px;font-size:8px;color:var(--dark)}
.phone{right:96px;top:27px;font-size:21px;color:var(--red)}
.mail{right:96px;top:57px;font-size:10.5px;color:#444}
.hero{left:0;top:100px;width:900px;height:400px;background:radial-gradient(ellipse at 60% 80%,#7a6a55 0%,#3b4250 35%,#232a36 75%)}
.swoosh{left:0;top:360px}
.main-nav{left:97px;top:152px;width:151px;height:215px;background:rgba(255,255,255,.96);padding:8px 14px 0 12px}
.main-nav li{list-style:none;font-size:12px;color:#222;height:20.3px;line-height:20px;border-bottom:1px solid #dcdcdc;padding-left:15px;position:relative}
.main-nav li:last-child{border-bottom:none}
.main-nav li::before{content:"";position:absolute;left:2px;top:8px;border:3px solid transparent;border-left:4px solid var(--red)}
.caption{left:277px;top:301px;width:525px;height:66px;background:rgba(30,30,30,.78);color:#fff;font-size:18.5px;text-align:right;padding:7px 13px;line-height:26px}
.slide-arrows{left:754px;top:367px;width:48px;height:20px;background:var(--red)}
.col h2{font-size:16px;font-weight:400;color:var(--red);letter-spacing:.3px;margin-bottom:8px}
.col ul{list-style:none}
.col li{font-size:9.5px;line-height:13.6px;padding:4px 0 4px 16px;position:relative;color:#333}
.col li::before{content:"";position:absolute;left:2px;top:7px;width:6px;height:6px;border-radius:50%;background:var(--red)}
.more{font-size:9.5px;font-weight:700;color:var(--red);margin-top:14px;display:block}
.band{left:0;top:695px;width:900px;height:387px;background:linear-gradient(#e6e6e9,#f3f3f5 12%,#f0f0f2)}
.sec-title{font-size:16px;color:var(--red);font-weight:400}
.welcome{left:99px;top:730px;width:450px}
.welcome p{font-size:9.5px;line-height:17.2px;margin-top:7px;color:#333}
.hr{height:1px;background:var(--rule)}
.partners{left:97px;top:894px;display:flex;gap:6px}
.partner{width:112px;height:76px;background:#fff;border:1px solid #ddd;display:flex;align-items:center;justify-content:center;gap:6px;font-size:11px;font-weight:700;color:#555}
.partner i{width:10px;height:10px;background:var(--red);display:block}
.news{left:99px;top:988px;width:465px}
.news p{font-size:9.5px;line-height:17.4px;margin-top:7px;color:#333}
.news em{color:var(--red)}
.services{left:577px;top:734px;width:226px;height:334px;background:#fff;border:1px solid #ddd;border-radius:3px;padding:10px 14px}
.services .photo{width:199px;height:101px;margin-top:8px;background:linear-gradient(135deg,#2f5d8f,#9bb2c8 55%,#c9b98c)}
.services ul{list-style:none;margin-top:8px}
.services li{font-size:9px;line-height:17.3px;padding-left:18px;position:relative;color:#444}
.tick{position:absolute;left:0}
.site-footer{left:0;top:1082px;width:900px;height:118px;background:var(--footer)}
.foot-brand{left:97px;top:22px;display:flex;align-items:center;gap:6px;color:#e5e5e5;font-size:16px;font-weight:700}
.foot-brand i{width:14px;height:14px;background:#e5e5e5;display:block}
.copy{left:99px;top:75px;font-size:9px;color:#ccc}
.social{left:559px;display:flex;align-items:center;gap:13px;color:#ddd;font-size:11px}
.social .ico{width:26px;height:26px;background:#1f1f1f;border:1px solid #555;border-radius:3px;display:flex;align-items:center;justify-content:center}
</style>
</head>
<body>
<header class="site-header abs">
  <div class="brand abs"><span class="brand-mark"></span><span class="brand-name">Bright Harbour Consulting</span></div>
  <div class="brand-tag abs">Providing Effective Project Controls and Management Solutions</div>
  <div class="phone abs">+61 0400 555 019</div>
  <div class="mail abs">hello@brightharbourconsulting.example</div>
</header>

<section class="hero abs" role="img" aria-label="Industrial refinery towers lit at dusk"></section>
<svg class="swoosh abs" width="900" height="140" viewBox="0 0 900 140">
  <path d="M0 8 Q450 150 900 10 L900 140 L0 140Z" fill="var(--red)"/>
  <path d="M0 36 Q450 165 900 36 L900 140 L0 140Z" fill="#c9c9cc"/>
  <path d="M0 52 Q450 180 900 50 L900 140 L0 140Z" fill="#9c9ca0"/>
  <path d="M0 62 Q450 200 900 60 L900 140 L0 140Z" fill="var(--dark)"/>
  <path d="M0 80 Q450 250 900 80 L900 140 L0 140Z" fill="var(--light)"/>
</svg>
<nav class="main-nav abs">
  <ul>
    <li>Home</li><li>Services</li><li>Benefits</li><li>Management</li><li>Planning</li>
    <li>Optimization</li><li>Industry</li><li>Software</li><li>Contact us</li><li>Recruitment</li>
  </ul>
</nav>
<div class="caption abs">Provide Effective Project Control &amp; Management Solutions to Projects within Australia and Overseas.</div>
<svg class="slide-arrows abs" viewBox="0 0 48 20"><path d="M18 5 L13 10 L18 15 M30 5 L35 10 L30 15" stroke="#fff" stroke-width="2" fill="none"/></svg>

<section class="col abs" style="left:96px;top:516px">
  <h2>BENEFITS</h2>
  <ul><li>Identify project risks</li><li>Stream line processes</li><li>Improving project visibility</li><li>Influencing project outcomes</li><li>Plan &amp; control budgets</li></ul>
  <span class="more">READ MORE &gt;&gt;</span>
</section>
<section class="col abs" style="left:283px;top:516px;width:160px">
  <h2>MANAGEMENT</h2>
  <ul><li>Project Management</li><li>Program &amp; Portfolio Management</li><li>Independent Reviews and Governance</li><li>Project Controls Management Systems</li></ul>
  <span class="more">READ MORE &gt;&gt;</span>
</section>
<section class="col abs" style="left:482px;top:516px">
  <h2>PLANNING</h2>
  <ul><li>Project Planning and Scheduling</li><li>Cost Control</li><li>Forecasting</li><li>Data Analysis</li></ul>
  <span class="more">READ MORE &gt;&gt;</span>
</section>
<section class="col abs" style="left:674px;top:516px">
  <h2>OTIMISATION</h2>
  <ul><li>Progress and Performance</li><li>Equipment &amp; Resource</li><li>Reporting</li></ul>
  <span class="more">READ MORE &gt;&gt;</span>
</section>

<div class="band abs"></div>
<section class="welcome abs">
  <h2 class="sec-title">WELCOME TO BRIGHT HARBOUR CONSULTING</h2>
  <p>Bright Harbour Consulting provides effective project controls and management solutions for construction projects in Australia and Overseas. We provide services to both large multinational companies and smaller privately owned businesses. Our knowledge and expertise assist clients to effectively plan and manage their construction projects or project portfolios. Our focus is to provide your business with the tools, solutions and strategies necessary to deliver projects on time and within budget.</p>
  <div class="hr" style="margin-top:12px;width:465px"></div>
  <h2 class="sec-title" style="margin-top:10px">PROJECTS ASSOCIATED WITH</h2>
</section>
<div class="partners abs">
  <div class="partner"><i></i>Southcoast Gas</div>
  <div class="partner">Korvanta Fuels</div>
  <div class="partner">Ridgeline Alliance</div>
  <div class="partner">Westvale Resources</div>
</div>
<section class="news abs">
  <div class="hr" style="margin-bottom:10px"></div>
  <h2 class="sec-title">NEWS</h2>
  <svg class="abs" style="right:0;top:14px" width="36" height="14" viewBox="0 0 36 14"><path d="M8 2 L3 7 L8 12 M28 2 L33 7 L28 12" stroke="#444" stroke-width="1.6" fill="none"/></svg>
  <p>Aliquam molestie, mi et imperdiet euismod, dui purus auctor tellus, et interdum lacus lectus et ante. Sed accumsan sollicitudin sapien, sit amet adipiscing turpis gravida ac. ..<em>Read More</em></p>
</section>
<aside class="services abs">
  <h2 class="sec-title">SERVICES</h2>
  <div class="photo" role="img" aria-label="Engineers in hard hats reviewing a construction site"></div>
  <ul>
    <li style="color:#222"><span class="tick">✓</span>SUMMARY OF SERVICES PROVIDED</li>
    <li><span class="tick">✓</span>Governance &amp; assurance.</li>
    <li><span class="tick">✓</span>Tender preparation and reviews.</li>
    <li><span class="tick">✓</span>Project planning and scheduling.</li>
    <li><span class="tick">✓</span>Business process improvement.</li>
    <li><span class="tick">✓</span>Project and construction management.</li>
    <li><span class="tick">✓</span>Programme and portfolio management.</li>
    <li><span class="tick">✓</span>Independent reviews and risk analysis</li>
    <li><span class="tick">✓</span>Project support services</li>
  </ul>
  <span class="more" style="margin-top:10px">READ MORE &gt;&gt;</span>
</aside>

<footer class="site-footer abs">
  <div class="foot-brand abs"><i></i>Bright Harbour Consulting</div>
  <div class="copy abs">Copyright © 2013. All Right Reserved &nbsp;|&nbsp; Privacy Policy</div>
  <div class="social abs" style="top:14px"><span class="ico"></span>Follow Us on Circlebook</div>
  <div class="social abs" style="top:46px"><span class="ico"></span>Update &nbsp;with Us on Circlebook</div>
  <div class="social abs" style="top:78px"><span class="ico"><svg width="16" height="12" viewBox="0 0 16 12"><rect x=".5" y=".5" width="15" height="11" fill="none" stroke="#ddd"/><path d="M.5 .5 L8 7 L15.5 .5" fill="none" stroke="#ddd"/></svg></span>hello@brightharbourconsulting.example</div>
</footer>
</body>
</html>
```